Redesign and move to Wordpress for quarvendo.com

Our website needs a redesign and at the same time we are moving it to Wordpress. Please help us with a new digital professional look and feel.

We are an Australian Software Engineering company specialising in advanced software development using in A.I., PLatform Engineering, Integration and Cloud. See the current quarvendo.com for more information about us.

```html
<!DOCTYPE html>
<html lang="en">
<head>
<meta charset="utf-8">
<title>Quarvendo – Reliable Smart Software Engineering</title>
<link rel="stylesheet" href="https://fonts.googleapis.com/css2?family=Montserrat:wght@300;400;500;600;700&family=Roboto:wght@400;500;700&display=swap">
<style>
:root{
  --topbar:#a47af2;
  --nav:#232323;
  --navy:#1d2b5a;
  --blue:#1e6fb8;
  --button:#1565c0;
  --band-a:#2b5b8e;
  --band-b:#1467bf;
  --slate:#455d7a;
  --card:#ffffff;
  --muted:#6b6b6b;
  --grey-band:#e6e6e6;
  --link:#3a5bd1;
  --text:#2b2b2b;
  --tint:#dde7fb;
}
*{box-sizing:border-box;margin:0;padding:0}
html,body{width:1200px;height:4189px;overflow:hidden}
body{position:relative;background:#fff;font-family:"Roboto",Arial,sans-serif;color:var(--text)}
.abs{position:absolute}

/* top bar */
.topbar{left:0;top:0;width:1200px;height:44px;background:var(--topbar);color:#fff;font:500 14px "Roboto",sans-serif;display:flex;align-items:center;padding:0 32px;justify-content:space-between}
.topbar .phone{display:flex;align-items:center;gap:10px}
.topbar .social{display:flex;gap:20px}
.topbar .social span{width:14px;height:14px;border-radius:50%;background:#fff;display:block}

/* nav */
.nav{left:0;top:44px;width:1200px;height:93px;background:var(--nav)}
.brand{position:absolute;left:28px;top:26px;display:flex;align-items:center;gap:12px;color:#fff;font:400 30px "Montserrat",sans-serif;letter-spacing:1px}
.brand i{display:block;width:34px;height:34px;border:3px solid #fff}
.menu{position:absolute;left:474px;top:35px;display:flex;gap:0;font:400 15px "Roboto",sans-serif;color:#fff}
.menu a{color:#fff;text-decoration:none;padding:4px 14px 8px}
.menu a.active{border-bottom:2px solid #8fa9e8}
.search{position:absolute;left:933px;top:26px;width:246px;height:44px;display:flex}
.search .field{flex:1;background:#fff;border-radius:6px 0 0 6px;font:14px "Roboto",sans-serif;color:#888;padding:14px 12px}
.search .go{width:46px;background:#8b4fe8;border-radius:0 6px 6px 0;display:flex;align-items:center;justify-content:center}

/* hero */
.hero{left:0;top:137px;width:1200px;height:421px;background:radial-gradient(ellipse at 60% 45%,#2a6cf2 0%,#1238b0 35%,#0a1a6a 70%,#060d3d 100%)}
.hero h1{position:absolute;left:47px;top:165px;color:#fff;font:400 37px/1.15 Arial,"Roboto",sans-serif}
.hero .dots{position:absolute;left:586px;top:404px;display:flex;gap:14px}
.hero .dots span{width:6px;height:6px;border-radius:50%;background:#fff;opacity:.7}

/* welcome */
.welcome h2{left:47px;top:612px;font:500 36px "Montserrat",sans-serif;color:var(--navy)}
.welcome p{left:47px;top:702px;width:520px;font:400 14.5px/1.68 "Roboto",sans-serif;color:#444}
.btn{left:47px;top:865px;width:119px;height:39px;background:var(--button);color:#fff;font:700 11px "Roboto",sans-serif;display:flex;align-items:center;justify-content:center;letter-spacing:.5px}
.welcome-photo{left:632px;top:605px;width:568px;height:320px;border-radius:24px 0 0 24px;background:linear-gradient(120deg,#1c2a3c 0%,#4b6a8c 40%,#c9d3dd 70%,#e9ecef 100%)}

/* services */
.service-band{left:0;top:1000px;width:1200px;height:224px;border-radius:14px 14px 0 0;background:linear-gradient(180deg,var(--band-a),var(--band-b))}
.service-band .eyebrow{position:absolute;left:19px;top:71px;color:#fff;font:600 16px "Montserrat",sans-serif;letter-spacing:4px}
.service-band h2{position:absolute;left:19px;top:114px;color:#fff;font:600 33px "Montserrat",sans-serif}
.service-grid{left:0;top:1224px;width:1200px;height:987px;background:var(--slate)}
.card{position:absolute;width:246px;background:var(--card);box-shadow:0 4px 10px rgba(0,0,0,.25);text-align:center;padding:26px 24px 0}
.card svg{width:58px;height:58px}
.card h3{margin-top:26px;font:500 20px/1.4 "Montserrat",sans-serif;color:var(--blue);letter-spacing:.3px}
.card p{margin-top:14px;text-align:left;font:400 13.5px/1.75 "Montserrat",sans-serif;color:var(--muted)}
.card .wordmark{height:58px;font:500 30px "Montserrat",sans-serif;color:#c9cfd8;letter-spacing:3px;line-height:58px}

/* clients */
.client{top:2345px;width:240px;text-align:center;font:700 38px "Montserrat",sans-serif;color:#2d2d2d;letter-spacing:-1px}
.client.sm{font-size:24px;letter-spacing:0;top:2355px}

/* news */
.news-band{left:0;top:2528px;width:1200px;height:225px;background:var(--grey-band);border-radius:14px 14px 0 0}
.news-band .eyebrow{position:absolute;left:19px;top:74px;font:500 15px "Montserrat",sans-serif;letter-spacing:4px;color:#222}
.news-band h2{position:absolute;left:19px;top:108px;font:500 40px "Montserrat",sans-serif;color:#111}
.article{position:absolute;background:linear-gradient(180deg,var(--tint) 0%,var(--tint) 70%,#fff 100%);padding:18px 10px 0;font:400 13.6px/1.66 "Roboto",sans-serif;color:#333}
.article h3{font:600 29px/1.02 "Montserrat",sans-serif;color:#111;margin-bottom:20px}
.article a{color:var(--link);text-decoration:underline;display:block;margin-bottom:12px}
.article p{margin-bottom:18px}
.article .gap{height:18px}
.article.center{text-align:center}
.article.tight p{margin-bottom:18px}
.article.tight a{margin-bottom:4px}
.servers{left:423px;top:2837px;width:354px;height:342px;background:linear-gradient(160deg,#f3f3f3,#c8c8c8 50%,#eeeeee)}
</style>
</head>
<body>

<header>
  <div class="abs topbar">
    <div class="phone">
      <svg width="16" height="16" viewBox="0 0 24 24" fill="none" stroke="#fff" stroke-width="2"><path d="M5 3h4l2 5-3 2a12 12 0 0 0 6 6l2-3 5 2v4a2 2 0 0 1-2 2A18 18 0 0 1 3 5a2 2 0 0 1 2-2z"/></svg>
      <span>1800 555 017</span>
    </div>
    <div class="social"><span></span><span></span><span></span></div>
  </div>
  <nav class="abs nav">
    <div class="brand"><i></i>quarvendo</div>
    <div class="menu">
      <a class="active">Home</a><a>Services</a><a>Contact</a><a>About</a><a>Blog</a>
    </div>
    <div class="search">
      <div class="field">Search ...</div>
      <div class="go"><svg width="18" height="18" viewBox="0 0 24 24" fill="none" stroke="#fff" stroke-width="3"><circle cx="10" cy="10" r="6"/><path d="M15 15l6 6"/></svg></div>
    </div>
  </nav>
</header>

<section class="abs hero" role="img" aria-label="Glowing blue circuit board traces on a dark background">
  <h1>Reliable Smart Software<br>Engineering</h1>
  <div class="dots"><span></span><span></span></div>
</section>

<section class="welcome">
  <h2 class="abs">Welcome to Quarvendo</h2>
  <p class="abs">At Quarvendo, we craft bespoke software solutions that are not available on the market. By building organizations market-leading products, process automation, legacy system enablement, or advanced intelligent systems, we empower our customers to achieve a competitive edge in their industry.</p>
  <div class="abs btn">SEE HOW</div>
  <div class="abs welcome-photo" role="img" aria-label="Engineer working at a computer in a robotics lab"></div>
</section>

<section>
  <div class="abs service-band">
    <div class="eyebrow">OUR SERVICE</div>
    <h2>We're Here To Make Your Software .</h2>
  </div>
  <div class="abs service-grid">
    <div class="card" style="left:65px;top:48px;height:374px">
      <svg viewBox="0 0 48 48" fill="none" stroke="#333" stroke-width="2"><rect x="8" y="14" width="32" height="24" rx="2"/><circle cx="24" cy="26" r="6"/><path d="M24 16v4M24 32v4M14 26h4M30 26h4M18 10h12"/></svg>
      <h3>ENTERPRISE Systems Integration</h3>
      <p>Automate your business processes internally or externally to improve data quality and process efficiency</p>
    </div>
    <div class="card" style="left:340px;top:48px;height:374px">
      <svg viewBox="0 0 48 48" fill="none" stroke="#333" stroke-width="2"><circle cx="24" cy="24" r="6"/><circle cx="24" cy="6" r="3"/><circle cx="24" cy="42" r="3"/><circle cx="6" cy="24" r="3"/><circle cx="42" cy="24" r="3"/><circle cx="11" cy="11" r="3"/><circle cx="37" cy="37" r="3"/><path d="M24 9v9M24 30v9M9 24h9M30 24h9M13 13l6 6M29 29l6 6"/></svg>
      <h3>Microservices</h3>
      <p>Leverage Microservices Architecture to enable quick deployment, dynamically scalable service performance, team productivity and more</p>
    </div>
    <div class="card" style="left:613px;top:48px;height:374px">
      <svg viewBox="0 0 48 48" fill="none" stroke="#333" stroke-width="2"><path d="M12 26a8 8 0 0 1 2-16 11 11 0 0 1 21 2 7 7 0 0 1 1 14z"/><rect x="16" y="18" width="16" height="14"/><path d="M16 23h16M16 28h16M20 32v6M28 32v6M14 40h20"/></svg>
      <h3>Plateform Engineering</h3>
      <p>For organisations looking to manage the security and cost risks around their cloud infrastructure management for applications</p>
    </div>
    <div class="card" style="left:888px;top:48px;height:374px">
      <svg viewBox="0 0 48 48" fill="none" stroke="#333" stroke-width="2"><rect x="22" y="4" width="20" height="14" rx="3"/><rect x="8" y="18" width="22" height="22" rx="4"/><circle cx="15" cy="27" r="2"/><circle cx="23" cy="27" r="2"/><path d="M15 34h8M27 11h2M32 11h2M37 11h2"/></svg>
      <h3>Conversational AI</h3>
      <p>Enabling legacy systems with conversational user interfaces, or simply building intelligent natural language based services, conversational AI has many use cases across sales and operations.</p>
    </div>

    <div class="card" style="left:65px;top:461px;height:478px">
      <svg viewBox="0 0 48 48" fill="none" stroke="#333" stroke-width="2"><rect x="6" y="8" width="36" height="26" rx="2"/><circle cx="18" cy="30" r="7"/><circle cx="18" cy="30" r="2.5"/><path d="M28 16h10M28 22h10M10 16h10"/></svg>
      <h3>IPaaS</h3>
      <p>Integration Platform as a Service brings the power of cloud based services to traditional systems integration. This is the new integration approach that enables quick, efficient and reliable enterprise systems integration</p>
    </div>
    <div class="card" style="left:340px;top:461px;height:478px">
      <svg viewBox="0 0 48 48" fill="none" stroke="#333" stroke-width="2"><path d="M16 42v-8a14 14 0 1 1 18-4l2 6h-6v6z"/><circle cx="24" cy="18" r="2"/><circle cx="20" cy="24" r="2"/><circle cx="28" cy="24" r="2"/><path d="M24 20l-3 3M24 20l3 3"/></svg>
      <h3>AI Assist / AI Agents</h3>
      <p>The future of business AI are autonomous agents that specialise in your business data and processes. Not only doing the current work well, but enabling intelligence and insight along the way</p>
    </div>
    <div class="card" style="left:613px;top:461px;height:478px">
      <svg viewBox="0 0 48 48" fill="none" stroke="#333" stroke-width="2"><rect x="6" y="6" width="18" height="14"/><rect x="26" y="14" width="16" height="12"/><circle cx="32" cy="36" r="6"/><circle cx="14" cy="34" r="5"/><path d="M15 20v9M24 14h2"/></svg>
      <h3>Real-Time Data Stream Processing</h3>
      <p>Being able to react to changing business conditions in a precise intelligent way is becoming increasingly important. Knowing how to manage real-time data streams around your organisation is the key to unlocking this capability</p>
    </div>
    <div class="card" style="left:888px;top:461px;height:478px">
      <div class="wordmark">glidely</div>
      <h3>Custom Integration For Small To Medium Business</h3>
      <p>Our expertise in platform engineering, iPaaS, building distributed systems and enterprise systems integration has converted into a product offering helping small to medium business solve their own complex systems integration problems</p>
    </div>
  </div>
</section>

<section class="clients">
  <div class="abs client" style="left:56px">ORVELL</div>
  <div class="abs client sm" style="left:366px">Brightmere</div>
  <div class="abs client sm" style="left:652px">TANDREL</div>
  <div class="abs client sm" style="left:938px;font-weight:500">kelvora</div>
</section>

<section>
  <div class="abs news-band">
    <div class="eyebrow">Updates from our industry</div>
    <h2>NEWS &amp; ARTICLES</h2>
  </div>

  <article class="article" style="left:28px;top:2837px;width:366px;height:602px">
    <h3>AI in software engineering</h3>
    <a>10 unexpected ways to use CodeWing Assist</a>
    <p>(CodeWing Blog) CodeWing Assist is widely known for its code generation feature. Learn how the AI assistant's abilities can extend beyond just code generation.</p>
    <div class="gap"></div>
    <h3>Business insights</h3>
    <a>How Storytelling Helps Data-driven Teams Succeed</a>
    <p><b>(Halden School of Management)</b> Winning leaders know that data alone isn't enough. It's the art of storytelling that drives sustained performance. In the spring of 2014, the Bayside Comets hired Sam Carrow as their head coach. Despite a star-studded roster, they hadn't won a Pro Hoops League championship in 40 years. Carrow changed the system, combining talent with authentic storytelling. The result? An era of league domination!</p>
  </article>

  <div class="abs servers" role="img" aria-label="Rows of computer server towers connected by black cables"></div>

  <article class="article" style="left:805px;top:2837px;width:366px;height:602px">
    <h3>Industry research</h3>
    <a>PROMPTIX: A general-purpose framework for prompt optimization</a>
    <p>(Brightmere Research) Large language models (LLMs) have revolutionized various tasks, but prompt engineering remains a challenge. Enter PROMPTIX: an open-source tool that streamlines prompt optimization, especially for complex structures like Retrieval Augmented Generation (RAG).</p>
    <a>The Power of Prompting</a>
    <p>(Brightmere Research) Brightmere discusses Prompting strategies that demonstrates how the generalist Lumen-4 model can perform as a specialist on medical challenge problem benchmarks. The study shows Lumen-4's ability to outperform a leading model that was fine-tuned specifically for medical applications, on the same benchmarks and by a significant margin.</p>
  </article>

  <article class="article tight" style="left:28px;top:3540px;width:362px;height:598px">
    <h3>Corelane &amp; Skyvault</h3>
    <a>What's new Corelane 9</a>
    <p>(Brightmere Learning) Learn about the improvements coming in this beta release. ML.Corelane, Vela and more...</p>
    <a>Lumen-4o: Northlight AI's new flagship multimodal model now in preview on Skyvault.</a>
    <p>(Brightmere Blog) This groundbreaking multimodal model integrates text, vision, and audio capabilities, setting a new standard for generative and conversational AI experiences.</p>
    <a>What's new Corelane 8</a>
    <p>(Brightmere Learning) The successor to Corelane 7, understand the runtime improvements, what's new in the SDK, Vela 12, Corelane Harbor, Corelane UI and more...</p>
  </article>

  <article class="article center tight" style="left:420px;top:3540px;width:360px;height:598px">
    <h3 style="text-align:left">Artificiall Intelligence</h3>
    <a>Advancing transparency: Updates on responsible AI research</a>
    <p>(Brightmere Research) A surge of generative AI models in the past year has fueled much discussion about the impact of artificial intelligence on human history. Advances in AI have indeed challenged thinking across industries, from considering how people will function in creative roles to effects in education, medicine, manufacturing, and more. Whether exploring impressive new capabilities of large language models (LLMs) such as Lumen-4 or examining the spectrum of machine learning techniques already embedded in our daily lives, researchers agree on the importance of transparency.</p>
  </article>

  <article class="article tight" style="left:808px;top:3540px;width:363px;height:598px">
    <h3>Conversational Interface</h3>
    <a>Choose the right chatbot solution for your use case</a>
    <p>(Brightmere Learning) A chatbot is an application that has written or spoken natural language as its user interface. In other words, a conversation is the means through which questions are answered, requests are serviced, and so on.</p>
    <a>Choose a Skyvault Cognitive Services technology</a>
    <p>(Brightmere Learning) Skyvault Cognitive Services is a set of cloud-based APIs that you can use in AI applications and data flows. It provides pretrained models that are ready to use in your applications, requiring no data and no model training on your part. The services are developed by the Brightmere AI and Research team and expose the latest deep learning algorithms.</p>
  </article>
</section>

</body>
</html>
```